New Business Card Design Project

The idea, the card is to put a card, which contains two companies at the same time. Please see the attached data and idea of how the current cards are.
VELMIR
Constructora
Ferrepiezas Caliza SRL.
Equipos para Plantas de Tratamientos y Acueductos, Alquiler de Equipos Pesados para la Construcción.
C / Tomás Urbina No.47
Barrio Lucero, Santo Domingo. República Dominicana.
Tel .: 1809 512 4476
CEL: 1829 746 2158
oriol@ferrepiezascaliza.example
velmirconstrution@correo-ejemplo.example
www.ferrepiezascaliza.example
Velmir construction.
Es una empresa constructora.
NOTA: La idea es llevar una sola tarjeta para dos compañías. o si no resulta hacer un diseño en cada lado, uno para cada empresa.Equipos para Plantas de Tratamiento y Acueductos, Alquiler de Equipos Pesados para la Construcción.
Deben de llevar, los logos.
VELMIR
Constructora
Ferrepiezas Caliza SRL.
C / Tomás Urbina No.47
Tel .: 1809 512 4476
CEL: 1829 746 2158
Velmir construction.
VELMIR
Constructora
Ferrepiezas Caliza SRL.
C / Tomás Urbina No.47
Tel .: 1809 512 4476
CEL: 1829 746 2158
Velmir construction.
It is a construction company
NOTE: The idea is to carry a single card for two companies. or if it does not turn out to make a design on each side, one for each company. Equipment for Treatment Plants and Aqueducts, Rental of Heavy Equipment for Construction.
They must carry, the logos.
How is the design similar to that, send example, for data, from previous designs.
What I'm looking for is a new design, not a remodeled copy
ferrepiezascaliza
Tel: 1809 542 4476
cel: 1829 746 2158
oriol@gerrepiezascaliza.example
Direccion:
C/ Tomás Urbina # 47
Barrio lucero, Santo Domingo
Republica Dominicana
Velmir
constructora
Tel: 1809 358-1047
Cel: 1829 746 2158
velmirsa1@correo-ejemplo.example
Direccion:
C/ Tomás Urbina # 47
Republica Dominicana
FERREPIEZAS CALIZA, S.R.L.
C/ Ramiro Olmedo Lasta esquina Tomás Urbina # 47
Barrio Lucero, Santo Domingo, República Dominicana
Office: 809.542.4476
Fax: 809.594.7361
Cel (Local): 829 746 2158
E-mail: MUESTRA@MUESTRA.example
E-mail:MUESTRA@correo-ejemplo.example
Website: http://www.MUESTRA.example

```html
<!DOCTYPE html>
<html lang="es">
<head>
<meta charset="utf-8">
<title>Ferrepiezas Caliza y Velmir Constructora — Tarjeta de presentación</title>
<link rel="stylesheet" href="https://fonts.googleapis.com/css2?family=Roboto:wght@400;500;700&display=swap">
<style>
  :root {
    --backdrop: #8c8c8c;
    --brand-blue: #0b4c8a;
    --brand-yellow: #f7c021;
    --paper-white: #ffffff;
    --rule-blue: #7fa6cf;
  }
  html, body {
    margin: 0;
    padding: 0;
    width: 1200px;
    height: 1200px;
    overflow: hidden;
    background: var(--backdrop);
    font-family: "Roboto", Arial, sans-serif;
  }
  .canvas {
    position: relative;
    width: 1200px;
    height: 1200px;
  }
  .card {
    position: absolute;
    top: 310px;
    height: 594px;
    background: var(--brand-blue);
    overflow: hidden;
    box-shadow: 2px 3px 6px rgba(0,0,0,0.35);
    color: var(--paper-white);
    text-align: center;
  }
  .card--front { left: 234px; width: 364px; }
  .card--back { left: 627px; width: 369px; }

  .front-brands {
    position: absolute;
    top: 88px;
    left: 0;
    right: 0;
    font-weight: 700;
    font-size: 22px;
    line-height: 27px;
    letter-spacing: 0.5px;
    color: var(--paper-white);
  }
  .front-brands .brand + .brand {
    margin-top: 16px;
    padding-top: 16px;
    border-top: 1px solid var(--rule-blue);
    margin-left: 92px;
    margin-right: 92px;
  }
  .person-name {
    position: absolute;
    top: 280px;
    left: 0; right: 0;
    font-size: 26px;
    font-weight: 700;
    color: var(--brand-yellow);
    line-height: 30px;
  }
  .person-title {
    position: absolute;
    top: 307px;
    left: 0; right: 0;
    font-size: 17px;
    line-height: 20px;
  }
  .rule {
    position: absolute;
    left: 42px;
    width: 280px;
    height: 1px;
    background: var(--rule-blue);
  }
  .rule--top { top: 333px; }
  .rule--bottom { top: 432px; }
  .contact-list {
    position: absolute;
    top: 341px;
    left: 0; right: 0;
    font-size: 17px;
    line-height: 20.3px;
  }
  .contact-list .label { color: var(--brand-yellow); font-weight: 500; }
  .company-block {
    position: absolute;
    top: 441px;
    left: 0; right: 0;
    font-size: 17px;
    line-height: 20px;
  }
  .company-block .company-name {
    color: var(--brand-yellow);
    font-weight: 700;
  }
  .company-block .city { margin-top: 10px; }

  .back-disc {
    position: absolute;
    left: 0;
    top: 0;
  }
  .back-partner {
    position: absolute;
    top: 214px;
    left: 0; right: 0;
    font-size: 17px;
    font-weight: 700;
    line-height: 20px;
    letter-spacing: 1px;
    color: var(--brand-blue);
  }
  .back-name {
    position: absolute;
    top: 286px;
    left: 0; right: 0;
    font-size: 28px;
    font-weight: 700;
    line-height: 32px;
    color: var(--brand-blue);
  }
  .back-web {
    position: absolute;
    top: 536px;
    left: 0; right: 0;
    font-size: 17px;
    color: var(--paper-white);
  }
</style>
</head>
<body>
<main class="canvas">

  <section class="card card--front">
    <div class="front-brands">
      <div class="brand">FERREPIEZAS<br>CALIZA</div>
      <div class="brand">VELMIR<br>CONSTRUCTORA</div>
    </div>
    <div class="person-name">ORIOL VENTURA</div>
    <div class="person-title">Managing Director</div>
    <div class="rule rule--top"></div>
    <div class="contact-list">
      <div><span class="label">P :</span> 809.542.4476 | <span class="label">F :</span> 809.594.7361</div>
      <div><span class="label">M :</span> 829 746 2158(Local)</div>
      <div><span class="label">E :</span> MUESTRA@MUESTRA.example</div>
      <div><span class="label">E :</span> MUESTRA@correo-ejemplo.example</div>
    </div>
    <div class="rule rule--bottom"></div>
    <div class="company-block">
      <div class="company-name">FERREPIEZAS CALIZA, S.R.L.</div>
      <div>C/ Ramiro Olmedo Lasta</div>
      <div>esquina Tomás Urbina # 47</div>
      <div class="city">Barrio Lucero, Santo Domingo</div>
      <div>República Dominicana</div>
    </div>
  </section>

  <section class="card card--back">
    <svg class="back-disc" width="369" height="594" viewBox="0 0 369 594" aria-hidden="true">
      <circle cx="184" cy="307" r="182" fill="var(--paper-white)"/>
    </svg>
    <div class="back-partner">VELMIR<br>CONSTRUCTORA</div>
    <div class="back-name">FERREPIEZAS<br>CALIZA,S.R.L</div>
    <div class="back-web">www.ferrepiezascaliza.example</div>
  </section>

</main>
</body>
</html>
```